Bourbon label design for bourbon brand. Looking to freshen our current label.

I need a Bourbon label design for our rebranded Bourbon bottle. Label should include picture of our horse and our logo on the bottle. Front Label is 3.5 inches wide and 6 inches tall, back label is 4 inches tall and 3 inches wide. Back label can be a simple plain logo like the one in the brief. I have included a design of our current bottle and label. We want to stay close to the current color schemes but want a fresh rebrand of the design. The label needs to be the correct size on a tall bottle like pictured.

Target Market(s)

Our Bourbon members, 30-50 year old males

Requirements
Must have
• Picture of our horse, our B logo , straight Bourbon whiskey on the front. Room to edit text on the back label.

```html
<!DOCTYPE html>
<html lang="en">
<head>
<meta charset="utf-8">
<title>Nightfall Straight Bourbon Whiskey – Front Label</title>
<link rel="stylesheet" href="https://fonts.googleapis.com/css2?family=Crimson+Pro:wght@400;600&display=swap">
<style>
  :root {
    --label-black: #000000;
    --ink-white: #ffffff;
    --horse-light: #bdbdbd;
    --horse-mid: #8a8a8a;
    --horse-dark: #3a3a3a;
  }
  html, body {
    margin: 0;
    padding: 0;
    width: 700px;
    height: 1200px;
    overflow: hidden;
    background: var(--label-black);
  }
  .label {
    position: relative;
    width: 700px;
    height: 1200px;
    background: var(--label-black);
    color: var(--ink-white);
    font-family: "Crimson Pro", "Times New Roman", serif;
    overflow: hidden;
  }
  .label__est,
  .label__year {
    position: absolute;
    top: 164px;
    font-size: 25px;
    letter-spacing: 0.02em;
    line-height: 1;
  }
  .label__est { left: 100px; }
  .label__year { left: 533px; }

  .label__horse {
    position: absolute;
    left: 257px;
    top: 47px;
    width: 203px;
    height: 403px;
    border-radius: 90px 90px 40px 40px;
    background: radial-gradient(ellipse at 50% 35%, var(--horse-light) 0%, var(--horse-mid) 55%, var(--horse-dark) 100%);
  }

  .label__brand {
    position: absolute;
    left: 0;
    width: 700px;
    top: 478px;
    text-align: center;
    font-size: 104px;
    font-weight: 600;
    letter-spacing: 0.04em;
    line-height: 1.1;
  }
  .label__style {
    position: absolute;
    left: 0;
    width: 700px;
    top: 612px;
    text-align: center;
    font-size: 36px;
    font-weight: 400;
    line-height: 1.1;
  }

  .label__mark {
    position: absolute;
    left: 250px;
    top: 700px;
    width: 200px;
    height: 180px;
    display: flex;
    flex-direction: column;
    align-items: center;
    justify-content: center;
    gap: 14px;
  }
  .label__mark-dot {
    width: 70px;
    height: 70px;
    border-radius: 50%;
    background: var(--ink-white);
  }
  .label__mark-name {
    font-size: 28px;
    font-weight: 400;
    letter-spacing: 0.08em;
  }

  .label__feature {
    position: absolute;
    top: 853px;
    font-size: 20px;
    letter-spacing: 0.02em;
    line-height: 1;
  }
  .label__feature--barrel { left: 63px; }
  .label__feature--cask { left: 475px; }

  .spec {
    position: absolute;
    text-align: center;
  }
  .spec__title {
    display: block;
    font-size: 19px;
    letter-spacing: 0.05em;
    line-height: 1;
    margin-bottom: 5px;
  }
  .spec__box {
    display: block;
    background: var(--ink-white);
    border-radius: 6px;
  }
  .spec--barrel { left: 52px; top: 1034px; }
  .spec--barrel .spec__box { width: 135px; height: 46px; }
  .spec--aged { left: 290px; top: 1012px; }
  .spec--aged .spec__box { width: 120px; height: 79px; }
  .spec--abv { left: 513px; top: 1034px; }
  .spec--abv .spec__box { width: 136px; height: 46px; }
</style>
</head>
<body>
  <main class="label">
    <span class="label__est">EST</span>
    <span class="label__year">2016</span>

    <div class="label__horse" role="img" aria-label="Black and white photograph of the brand's racehorse galloping toward the viewer with a jockey aboard"></div>

    <h1 class="label__brand">NIGHTFALL</h1>
    <p class="label__style">Straight Bourbon Whiskey</p>

    <div class="label__mark">
      <span class="label__mark-dot"></span>
      <span class="label__mark-name">NIGHTFALL</span>
    </div>

    <span class="label__feature label__feature--barrel">SINGLE BARREL</span>
    <span class="label__feature label__feature--cask">CASK STRENGTH</span>

    <div class="spec spec--barrel">
      <span class="spec__title">BARREL NO.</span>
      <span class="spec__box"></span>
    </div>
    <div class="spec spec--aged">
      <span class="spec__title">AGED</span>
      <span class="spec__box"></span>
    </div>
    <div class="spec spec--abv">
      <span class="spec__title">ALC/VOL</span>
      <span class="spec__box"></span>
    </div>
  </main>
</body>
</html>
```